THE VELVET MOTHS DANCE CONCERT

Hello again! We need a Front Cover for our Dance Showcase Program. Our theme is year is "LEGENDS" .
We are paying Tribute to the Musical Legends through the years. TOBIN, DARRELL HUTTON, QUILLO, ZENA BOLT etc.
It should include:
1. our Name and Logo (three girls) , which we will provide.
2. Colorful and Bright, Flashy SUPERSTAR feel to it!
3. Size for Print is 8.25 by 10.75 (front page of a magazine type booklet)
4.It should Say somewhere:
" The Velvet Moths Dance Factory presents... "
LEGENDS
5. include "2023 Annual Showcase"
6. Include our website address somewhere : www.VMKSstudios.example
7: include " Follow us @VMKS (Snapvista Logo)
you have been working with us for a few years now. Thank you for sharing your gifts and art!
Music Lovers
Entertainment

```html
<!DOCTYPE html>
<html lang="en">
<head>
<meta charset="utf-8">
<title>LEGENDS – 2023 Annual Showcase</title>
<link rel="stylesheet" href="https://fonts.googleapis.com/css2?family=Limelight&family=Abril+Fatface&family=Archivo+Black&family=Montserrat:wght@500;600&display=swap">
<style>
  :root {
    --page: #f1f1f1;
    --night: #1c0a26;
    --plum: #3a1150;
    --violet: #6a1fa0;
    --orchid: #8e2bc4;
    --magenta: #d23a8c;
    --rose: #e84f9c;
    --white: #ffffff;
    --shade: #b0317a;
  }
  * { margin: 0; padding: 0; box-sizing: border-box; }
  html, body { width: 900px; height: 1200px; overflow: hidden; background: var(--page); }
  .cover {
    position: absolute; left: 10px; top: 26px;
    width: 880px; height: 1147px; overflow: hidden;
    background: linear-gradient(180deg, var(--night) 0%, var(--plum) 38%, var(--violet) 62%, var(--magenta) 88%, var(--rose) 100%);
    color: var(--white);
  }
  .backdrop, .frame { position: absolute; inset: 0; width: 880px; height: 1147px; }
  .presenter {
    position: absolute; left: 67px; top: 112px;
    font: 19px "Archivo Black", sans-serif; letter-spacing: 1px;
  }
  .wave { position: absolute; left: 672px; top: 116px; width: 190px; height: 30px; }
  .title {
    position: absolute; left: 68px; top: 142px;
    font: 122px "Limelight", serif; letter-spacing: 2px; line-height: 1;
  }
  .dancer-photo {
    position: absolute; left: 230px; top: 300px; width: 500px; height: 800px;
    background: radial-gradient(ellipse at 50% 40%, #f2d7c4 0%, #d8a98d 30%, rgba(120,60,90,0.6) 62%, rgba(60,20,70,0) 78%);
  }
  .dots { position: absolute; display: grid; grid-template-columns: repeat(6, 8px); gap: 12px; }
  .dots span { width: 8px; height: 8px; border-radius: 50%; background: var(--white); }
  .dots--left { left: 48px; top: 454px; }
  .dots--right { left: 612px; top: 903px; }
  .event { position: absolute; left: 40px; top: 835px; font-family: "Abril Fatface", serif; line-height: 1; text-shadow: 3px 3px 0 var(--shade); }
  .event__year { font-size: 92px; letter-spacing: 2px; }
  .event__name { font-size: 60px; margin-top: 2px; }
  .event__kind { font-size: 46px; margin-top: 6px; }
  .footer { position: absolute; left: 36px; top: 1086px; display: flex; gap: 26px; font: 600 13px "Montserrat", sans-serif; }
  .footer__item { display: flex; align-items: center; gap: 8px; }
  .footer__square { width: 20px; height: 20px; border: 2px solid var(--white); border-radius: 5px; }
  .footer__globe { width: 20px; height: 20px; }
  .brand {
    position: absolute; left: 738px; top: 960px; width: 125px; text-align: center;
    font: 17px "Archivo Black", sans-serif; line-height: 1.25;
  }
  .brand__mark { width: 34px; height: 34px; border-radius: 50%; background: var(--white); margin: 0 auto 10px; }
</style>
</head>
<body>
  <main class="cover">
    <svg class="backdrop" viewBox="0 0 880 1147" aria-hidden="true">
      <polygon points="600,0 880,0 880,330" fill="#5a1a88" opacity="0.75"/>
      <polygon points="840,0 880,0 880,150 700,330" fill="#7a26b4" opacity="0.6"/>
      <polygon points="130,300 460,250 340,560" fill="#5b1d8c" opacity="0.7"/>
      <polygon points="560,360 880,280 880,760" fill="#6c21a8" opacity="0.6"/>
      <polygon points="0,620 300,700 0,1000" fill="#7d2ab5" opacity="0.55"/>
      <polygon points="620,700 880,820 720,1147" fill="#a8308f" opacity="0.5"/>
      <polygon points="150,900 520,980 260,1147" fill="#c23a98" opacity="0.45"/>
      <polyline points="180,640 330,560 480,640 630,560" fill="none" stroke="#8b4bd0" stroke-width="3" opacity="0.5"/>
      <polyline points="180,690 330,610 480,690 630,610" fill="none" stroke="#8b4bd0" stroke-width="3" opacity="0.4"/>
    </svg>

    <p class="presenter">The Velvet Moths Dance Factory presents..</p>
    <svg class="wave" viewBox="0 0 190 30" aria-hidden="true">
      <path d="M2 15 q12 -14 24 0 t24 0 t24 0 t24 0 t24 0 t24 0 t24 0 t20 0" fill="none" stroke="#fff" stroke-width="3"/>
    </svg>
    <h1 class="title">LEGENDS</h1>

    <div class="dots dots--left" aria-hidden="true">
      <span></span><span></span><span></span><span></span><span></span><span></span>
      <span></span><span></span><span></span><span></span><span></span><span></span>
      <span></span><span></span><span></span><span></span><span></span><span></span>
    </div>

    <div class="dancer-photo" role="img" aria-label="Photograph of a dancer in a white shirt and black leotard holding a high side kick"></div>

    <svg class="frame" viewBox="0 0 880 1147" aria-hidden="true">
      <polygon points="736,294 79,586 574,1100" fill="none" stroke="#fff" stroke-width="5"/>
    </svg>

    <div class="dots dots--right" aria-hidden="true">
      <span></span><span></span><span></span><span></span><span></span><span></span>
      <span></span><span></span><span></span><span></span><span></span><span></span>
      <span></span><span></span><span></span><span></span><span></span><span></span>
    </div>

    <div class="event">
      <p class="event__year">2023</p>
      <p class="event__name">Annual</p>
      <p class="event__kind">Showcase</p>
    </div>

    <div class="brand">
      <div class="brand__mark" aria-hidden="true"></div>
      The Velvet Moths Dance Factory
    </div>

    <footer class="footer">
      <span class="footer__item"><span class="footer__square" aria-hidden="true"></span>Follow us @VMKS</span>
      <span class="footer__item">
        <svg class="footer__globe" viewBox="0 0 20 20" aria-hidden="true">
          <circle cx="10" cy="10" r="8.5" fill="none" stroke="#fff" stroke-width="1.6"/>
          <ellipse cx="10" cy="10" rx="3.6" ry="8.5" fill="none" stroke="#fff" stroke-width="1.4"/>
          <line x1="1.5" y1="10" x2="18.5" y2="10" stroke="#fff" stroke-width="1.4"/>
        </svg>
        www.VMKSstudios.example
      </span>
    </footer>
  </main>
</body>
</html>
```